PROPERTY BROCHURE

Need an attractive layout and design for this multi-page brochure

Industry/Entity Type

Real Estate Development

Colors

Designer to choose colors to be used in the design.

```html
<!DOCTYPE html>
<html lang="en">
<head>
<meta charset="utf-8">
<title>Ridgeline Estates – Property Brochure Spread</title>
<link rel="stylesheet" href="https://fonts.googleapis.com/css2?family=PT+Sans:wght@400;700&display=swap">
<style>
  :root{
    --backdrop:#a7b9bf;
    --page-dark:#201e21;
    --teal:#3b7c87;
    --teal-deep:#2f6771;
    --panel:#efefef;
    --panel-edge:#e2e2e2;
    --ink:#2a2a2a;
    --black:#111111;
    --chart-red:#c4433f;
    --white:#ffffff;
  }
  *{box-sizing:border-box;margin:0;padding:0}
  html,body{width:1200px;height:566px;overflow:hidden}
  body{background:var(--backdrop);font-family:"PT Sans",Arial,sans-serif;color:var(--ink)}

  .spread{position:absolute;left:30px;top:33px;width:1140px;height:500px;display:flex;box-shadow:0 10px 24px rgba(0,0,0,.25)}
  .page{position:relative;width:570px;height:500px;background:var(--page-dark);overflow:hidden}
  .page--left::after,.page--right::after{content:"";position:absolute;top:0;bottom:0;width:26px;pointer-events:none}
  .page--left::after{right:0;background:linear-gradient(to left,rgba(0,0,0,.35),rgba(0,0,0,0))}
  .page--right::after{left:0;background:linear-gradient(to right,rgba(0,0,0,.35),rgba(0,0,0,0))}

  .frame{position:absolute;border:6px solid var(--teal);border-radius:14px 14px 0 0;border-bottom:none;overflow:hidden;background:var(--white)}
  .photo{width:100%;height:100%}

  .panel{position:absolute;background:linear-gradient(var(--panel),var(--panel-edge));border:4px solid var(--teal);border-top:none;border-radius:0 0 12px 12px}
  .panel h2{font-weight:700;color:var(--teal);text-transform:uppercase;letter-spacing:.2px}
  .panel p{font-size:9.6px;line-height:1.38}

  /* left page */
  .living-frame{left:16px;top:52px;right:0;bottom:0;border-right:none;border-radius:14px 0 0 0}
  .living-photo{background:linear-gradient(160deg,#cfd6d1 0%,#e6e2dc 35%,#b9604f 60%,#d9cfc5 85%,#bfae9e 100%)}
  .business-panel{left:72px;top:0;width:418px;height:178px;padding:14px 16px 0;text-align:center;z-index:2}
  .business-panel h2{font-size:15px;margin-bottom:8px}
  .business-panel p+p{margin-top:9px}

  /* right page */
  .city-panel{left:12px;right:12px;top:0;height:170px;display:flex;padding:18px 14px 0 18px;gap:30px}
  .city-copy{width:222px;text-align:center}
  .city-copy h2{font-size:15px;margin-bottom:6px}
  .city-copy p{text-align:justify;text-align-last:center}

  .growth-table{border-collapse:collapse;font-size:10.5px;width:196px;height:136px;align-self:flex-start;margin-top:2px}
  .growth-table th{background:var(--black);color:var(--white);text-align:left;padding:3px 5px;font-weight:700;font-size:10.5px;height:22px;border:1px solid var(--black)}
  .growth-table td{padding:0 5px;border:1px solid #555;background:var(--white)}
  .growth-table td.year{background:var(--teal-deep);color:var(--white);font-weight:700;border-color:#1f4d55}

  .station-frame{left:12px;top:214px;width:300px;bottom:0}
  .station-photo{background:linear-gradient(180deg,#c9d3dc 0%,#aebccb 40%,#c99a49 62%,#a7793a 82%,#6f6a63 100%)}

  .chart-frame{left:340px;top:254px;width:212px;bottom:0;padding:5px 5px 0}
  .chart{display:block;width:100%;height:100%;background:var(--white)}
  .chart-title{font:700 9px "PT Sans",Arial,sans-serif;fill:var(--black)}
  .axis-label{font:400 5.5px "PT Sans",Arial,sans-serif;fill:#333}
</style>
</head>
<body>
<div class="spread">

  <section class="page page--left">
    <div class="frame living-frame">
      <div class="photo living-photo" role="img" aria-label="Bright modern living room with white sofas, red rug and red feature wall"></div>
    </div>
    <div class="panel business-panel">
      <h2>Our Business/What We Do</h2>
      <p>Ridgeline Estates is a real estate development organisation that identifies and executes projects in metropolitan area of Melbourne. This projects offer investors the opportunity to obtain significant returns on investment above bank interest rates.</p>
      <p>Ridgeline Estates is committed to providing quality medium density accommodation solutions to address the housing shortage currently experienced by the Australian and New Zealand market.</p>
      <p>Our projects represent a seamless balance between the financial requirements of our investors and the housing needs of those living in the communities we touch.</p>
    </div>
  </section>

  <section class="page page--right">
    <div class="panel city-panel">
      <div class="city-copy">
        <h2>Melbourne, Victoria</h2>
        <p>Population growth in Melbourne is the strongest in the country at 3.2% over the year to June 2016 and is being driven by both strong overseas and interstate migration. Interstate migration increased 64% year-on-year (y-y) to June 2016 according to the Bureau of Regional Statistics. By the middle of this century it will overtake Sydney to be Australia's largest city.</p>
      </div>
      <table class="growth-table">
        <thead><tr><th>Year</th><th>Population</th><th>Growth rate</th></tr></thead>
        <tbody>
          <tr><td class="year">2011</td><td>3850000</td><td>n/a</td></tr>
          <tr><td class="year">2012</td><td>4090000</td><td>5.87%</td></tr>
          <tr><td class="year">2013</td><td>4180000</td><td>2.20%</td></tr>
          <tr><td class="year">2014</td><td>4250000</td><td>1.67%</td></tr>
          <tr><td class="year">2015</td><td>4530000</td><td>6.60%</td></tr>
          <tr><td class="year">2016</td><td>4670000</td><td>2.98%</td></tr>
          <tr><td class="year">2017</td><td>4820000</td><td>3.21%</td></tr>
        </tbody>
      </table>
    </div>

    <div class="frame station-frame">
      <div class="photo station-photo" role="img" aria-label="Historic domed railway station building under a cloudy sky"></div>
    </div>

    <div class="frame chart-frame">
      <svg class="chart" viewBox="0 0 190 240" preserveAspectRatio="none" role="img" aria-label="Victoria population growth area chart">
        <text class="chart-title" x="95" y="22" text-anchor="middle">Victoria Population Growth</text>
        <g stroke="#444" stroke-width=".5">
          <line x1="40" y1="40" x2="186" y2="40"/><line x1="40" y1="58" x2="186" y2="58"/>
          <line x1="40" y1="76" x2="186" y2="76"/><line x1="40" y1="94" x2="186" y2="94"/>
          <line x1="40" y1="112" x2="186" y2="112"/><line x1="40" y1="130" x2="186" y2="130"/>
          <line x1="40" y1="148" x2="186" y2="148"/>
        </g>
        <g class="axis-label" text-anchor="end">
          <text x="37" y="42">6,500,000</text><text x="37" y="60">6,000,000</text>
          <text x="37" y="78">5,500,000</text><text x="37" y="96">5,000,000</text>
          <text x="37" y="114">4,500,000</text><text x="37" y="132">4,000,000</text>
          <text x="37" y="150">3,500,000</text>
        </g>
        <path fill="var(--chart-red)" d="M40 132 L60 127 L80 121 L100 116 L120 110 L140 101 L155 93 L168 82 L178 69 L186 55 L186 148 L40 148 Z"/>
        <g class="axis-label" text-anchor="end">
          <text transform="translate(43 151) rotate(-90)">1981</text>
          <text transform="translate(55 151) rotate(-90)">1984</text>
          <text transform="translate(67 151) rotate(-90)">1987</text>
          <text transform="translate(79 151) rotate(-90)">1990</text>
          <text transform="translate(91 151) rotate(-90)">1993</text>
          <text transform="translate(103 151) rotate(-90)">1996</text>
          <text transform="translate(115 151) rotate(-90)">1999</text>
          <text transform="translate(127 151) rotate(-90)">2002</text>
          <text transform="translate(139 151) rotate(-90)">2005</text>
          <text transform="translate(151 151) rotate(-90)">2008</text>
          <text transform="translate(163 151) rotate(-90)">2011</text>
          <text transform="translate(175 151) rotate(-90)">2014</text>
          <text transform="translate(187 151) rotate(-90)">2016</text>
        </g>
      </svg>
    </div>
  </section>

</div>
</body>
</html>
```